Flyer design for webdesign company

create a flyer that can be printed or sent as an email. The flyer needs to be professional, modern and engaging.

Reason: opportunity for all designers to get their designs in.

Target Market(s)

business owners that do not have a website

Industry/Entity Type

It Company

Font styles to use
Sans Serif

```html
<!DOCTYPE html>
<html lang="en">
<head>
<meta charset="utf-8">
<title>Nova Websites Flyer</title>
<link href="https://fonts.googleapis.com/css2?family=Roboto:wght@300;400;700&family=Roboto+Condensed:wght@700&display=swap" rel="stylesheet">
<style>
  :root {
    --orange: #ea8a2e;
    --orange-light: #f3b06a;
    --orange-edge: #d97a22;
    --grey: #5f5f5f;
    --grey-text: #777777;
    --white: #ffffff;
    --wood-dark: #7a5d47;
    --wood-light: #b79a82;
  }
  * { box-sizing: border-box; margin: 0; padding: 0; }
  html, body { width: 1041px; height: 1200px; overflow: hidden; background: var(--white); }
  .flyer {
    position: relative; width: 1041px; height: 1200px; overflow: hidden;
    background: var(--white);
    font-family: "Roboto", Arial, sans-serif;
  }
  .brand {
    position: absolute; left: 52px; top: 150px;
    display: flex; align-items: center; gap: 10px;
  }
  .brand-dot { width: 26px; height: 26px; border-radius: 50%; background: var(--orange); }
  .brand-name { font-size: 32px; font-weight: 400; color: var(--orange); letter-spacing: 0.5px; }
  .contact {
    position: absolute; left: 324px; top: 68px;
    font-weight: 700; font-size: 26px; color: var(--grey); line-height: 34px; letter-spacing: 0.5px;
  }
  .headline {
    position: absolute; left: 322px; top: 138px;
    font-family: "Roboto Condensed", Arial, sans-serif; font-weight: 700;
    font-size: 54px; line-height: 48px; color: var(--orange); text-transform: uppercase;
  }
  .hero-photo {
    position: absolute; left: 53px; top: 252px; width: 932px; height: 380px;
    border-radius: 4px;
    background: linear-gradient(120deg, var(--wood-light) 0%, var(--wood-dark) 55%, #9c7f68 100%);
  }
  .price-badge {
    position: absolute; left: 777px; top: 242px; width: 258px; height: 258px;
    border-radius: 50%; background: var(--orange);
    border: 10px solid var(--orange-light);
    display: flex; align-items: center; justify-content: center; text-align: center;
    font-family: "Roboto Condensed", Arial, sans-serif; font-weight: 700;
    font-size: 58px; line-height: 52px; color: var(--white);
  }
  .benefit {
    position: absolute; height: 80px; display: flex; align-items: center; gap: 22px;
    font-size: 21px; line-height: 26px; color: var(--grey-text); font-weight: 300;
  }
  .benefit .tick { flex: none; width: 90px; height: 74px; }
  .benefit strong { font-weight: 700; color: var(--grey); }
  .col-left { left: 53px; width: 470px; }
  .col-right { left: 535px; width: 500px; }
  .row-1 { top: 648px; }
  .row-2 { top: 740px; }
  .row-3 { top: 832px; }
  .row-4 { top: 924px; }
  .footer-band {
    position: absolute; left: 0; top: 1026px; width: 1041px; height: 174px;
    background: var(--orange); text-align: center; color: var(--white);
    padding-top: 10px;
  }
  .footer-band .pitch { font-weight: 700; font-size: 25px; line-height: 31px; }
  .footer-band .pricing {
    margin-top: 2px;
    font-family: "Roboto Condensed", Arial, sans-serif; font-weight: 700;
    font-size: 48px; line-height: 46px; text-transform: uppercase;
  }
</style>
</head>
<body>
<main class="flyer">
  <div class="brand">
    <span class="brand-dot"></span>
    <span class="brand-name">novawebsites</span>
  </div>

  <div class="contact">
    <p>Call Today 1-800-555-0142</p>
    <p>www.novasitesdemo.com</p>
  </div>

  <h1 class="headline">Attract more customers<br>Make more money</h1>

  <div class="hero-photo" role="img" aria-label="Photo of an open laptop on a wooden desk beside a sheet of white paper"></div>

  <div class="price-badge">ONLY<br>3 $<br>A DAY!</div>

  <svg width="0" height="0" style="position:absolute">
    <defs>
      <symbol id="tick-box" viewBox="0 0 93 76">
        <rect x="1.5" y="1.5" width="90" height="73" rx="6" fill="#ea8a2e" stroke="#d97a22" stroke-width="2"/>
        <path d="M24 40 L40 55 L70 22" fill="none" stroke="#ffffff" stroke-width="10" stroke-linecap="round" stroke-linejoin="round"/>
      </symbol>
    </defs>
  </svg>

  <div class="benefit col-left row-1">
    <svg class="tick"><use href="#tick-box"/></svg>
    <p><strong>97%</strong> of people look online for<br>businesses.<br>You need a website!</p>
  </div>
  <div class="benefit col-left row-2">
    <svg class="tick"><use href="#tick-box"/></svg>
    <p><strong>You're losing many customers<br>by not having a website</strong></p>
  </div>
  <div class="benefit col-left row-3">
    <svg class="tick"><use href="#tick-box"/></svg>
    <p>Beat your competition with<br>better visibility and credibility</p>
  </div>
  <div class="benefit col-left row-4">
    <svg class="tick"><use href="#tick-box"/></svg>
    <p><strong>BEAUTIFUL WEBSITES</strong><br>AVAILABLE NOW</p>
  </div>

  <div class="benefit col-right row-1">
    <svg class="tick"><use href="#tick-box"/></svg>
    <p>Smart, clean website designs<br><strong>($3000 Value. No extra charge)</strong></p>
  </div>
  <div class="benefit col-right row-2">
    <svg class="tick"><use href="#tick-box"/></svg>
    <p>Limited to ONLY 4 WEBSITES<br>per area. Don't miss out!</p>
  </div>
  <div class="benefit col-right row-3">
    <svg class="tick"><use href="#tick-box"/></svg>
    <p>Social Media setup options<br>(search &amp; social networks)</p>
  </div>

  <footer class="footer-band">
    <p class="pitch">Stop wasting money on mailers and<br>print advertising.</p>
    <p class="pricing">Pricing:<br>Only $99/month</p>
  </footer>
</main>
</body>
</html>
```